This is for a plastic credit card type business card for handing out to clients. It only has the web

I'm looking for a two sided card. This will be printed on a credit card type plastic, ie rounded edges. On the one side is the design. On the other 10 Codes.

The front. A design that is funky but still appropriate for someone in their 30's to 60's The words "Venturers Pledge" "Dorit Velkin" must appear on the front. At the bottom in small writing (Portrait) is www.velkincorp.com

So I'm really looking for the design of the top of the card in making my decision.

On the back of the card in portrait is the following copy.

Heading in Bold is "Venturers Pledge"

I will always remember my WHY
I am an agent for growth and prosperity
I really deserve success in my life
I always stand up again
I will reach out for support on my journey
I will lend fellow entrepreneurs support on their journey
I have the gift of a flexible mind
I see opportunity where others don't
I use my fears to drive me forward
I see success and failure as a learning opportunity

AT THE BOTTOM OF BACK OF THE CARD IS

www.velkincorp.com

```html
<!DOCTYPE html>
<html lang="en">
<head>
<meta charset="utf-8">
<title>Venturers Pledge – Card Front and Back</title>
<link rel="stylesheet" href="https://fonts.googleapis.com/css2?family=Amaranth:wght@700&family=Open+Sans:ital,wght@0,400;0,600;1,400&display=swap">
<style>
  :root {
    --stage-light: #ffffff;
    --stage-dark: #505050;
    --ink: #111111;
    --white: #ffffff;
    --front-top: #1c1c1c;
    --front-left: #0a1118;
    --front-right: #0e0d0c;
    --front-bottom: #05080b;
    --back-mist: #dfe4ea;
    --back-steel: #7d8fa0;
    --back-deep: #1d3749;
    --card-radius: 17px;
  }
  * { box-sizing: border-box; margin: 0; padding: 0; }
  html, body { width: 1200px; height: 848px; overflow: hidden; }
  body {
    position: relative;
    background: linear-gradient(90deg, var(--stage-light) 0%, #bdbdbd 45%, var(--stage-dark) 100%);
    font-family: "Open Sans", Arial, sans-serif;
  }
  .card {
    position: absolute;
    top: 96px;
    width: 403px;
    height: 670px;
    border-radius: var(--card-radius);
    overflow: hidden;
  }
  .card-front { left: 149px; background: var(--front-bottom); }
  .card-back {
    left: 625px;
    background: linear-gradient(180deg, var(--white) 0%, var(--white) 47%, var(--back-mist) 58%, var(--back-steel) 80%, var(--back-deep) 100%);
  }
  .front-pattern { position: absolute; inset: 0; }
  .front-name, .front-title {
    position: absolute;
    left: 0; right: 0;
    text-align: center;
    color: var(--white);
    font-size: 21px;
    font-weight: 400;
  }
  .front-name { top: 176px; }
  .front-title { top: 554px; }
  .ribbon { position: absolute; left: 0; top: 0; }
  .ribbon-title {
    position: absolute;
    left: 73px; width: 251px;
    top: 65px; height: 33px;
    line-height: 33px;
    text-align: center;
    color: var(--white);
    font-family: "Amaranth", "Open Sans", sans-serif;
    font-weight: 700;
    font-size: 20px;
  }
  .pledge-list {
    position: absolute;
    left: 35px; right: 18px;
    top: 188px;
    list-style: none;
    color: var(--ink);
    font-style: italic;
    font-size: 18px;
    line-height: 24px;
  }
  .pledge-list li { padding-left: 15px; text-indent: -15px; }
  .pledge-list li::before { content: "•"; display: inline-block; width: 15px; text-indent: 0; font-style: normal; }
  .back-web {
    position: absolute;
    left: 0; right: 0;
    bottom: 22px;
    text-align: center;
    color: var(--white);
    font-size: 16px;
    font-weight: 600;
    letter-spacing: 0.5px;
  }
</style>
</head>
<body>
  <section class="card card-front">
    <svg class="front-pattern" width="403" height="670" viewBox="0 0 403 670" aria-hidden="true">
      <defs>
        <pattern id="fine-stripes" width="4" height="4" patternUnits="userSpaceOnUse" patternTransform="rotate(45)">
          <rect width="4" height="4" fill="var(--front-top)"/>
          <line x1="0" y1="0" x2="0" y2="4" stroke="#262626" stroke-width="1"/>
        </pattern>
      </defs>
      <polygon points="0,0 200,327 0,670" fill="var(--front-left)"/>
      <polygon points="403,0 200,327 403,670" fill="var(--front-right)"/>
      <polygon points="0,670 200,327 403,670" fill="var(--front-bottom)"/>
      <polygon points="14,0 389,0 200,327" fill="url(#fine-stripes)"/>
    </svg>
    <p class="front-name">Dorit Velkin</p>
    <p class="front-title">Venturers Pledge</p>
  </section>

  <section class="card card-back">
    <svg class="ribbon" width="403" height="150" viewBox="0 0 403 150" aria-hidden="true">
      <polygon points="115,46 290,46 283,43 122,43" fill="var(--ink)"/>
      <line x1="120" y1="47" x2="285" y2="47" stroke="var(--ink)" stroke-width="1"/>
      <polygon points="44,72 80,72 80,108 44,108 56,90" fill="var(--ink)"/>
      <polygon points="359,72 323,72 323,108 359,108 347,90" fill="var(--ink)"/>
      <rect x="73" y="65" width="257" height="33" fill="var(--ink)"/>
      <rect x="77" y="69" width="249" height="25" fill="none" stroke="var(--white)" stroke-width="1"/>
      <line x1="118" y1="107" x2="285" y2="107" stroke="var(--ink)" stroke-width="1.2"/>
      <polygon fill="var(--ink)" points="201,121 204.5,128.5 212.5,129 206.5,134.5 208.5,142 201,138 193.5,142 195.5,134.5 189.5,129 197.5,128.5"/>
      <polygon fill="var(--ink)" points="183,127 185,131.5 189.5,132 186,135 187,139.5 183,137 179,139.5 180,135 176.5,132 181,131.5"/>
      <polygon fill="var(--ink)" points="219,127 221,131.5 225.5,132 222,135 223,139.5 219,137 215,139.5 216,135 212.5,132 217,131.5"/>
    </svg>
    <h1 class="ribbon-title">Venturers Pledge</h1>
    <ul class="pledge-list">
      <li>I will always remember my WHY.</li>
      <li>I am an agent for growth and prosperity.</li>
      <li>I really deserve success in my life.</li>
      <li>I always stand up again.</li>
      <li>I will reach out for support on my journey.</li>
      <li>I will lend fellow entrepreneurs support on their journey.</li>
      <li>I have the gift of a flexible mind.</li>
      <li>I see opportunity where others don't.</li>
      <li>I use my fears to drive me forward.</li>
      <li>I see success and failure as a learning opportunity.</li>
    </ul>
    <p class="back-web">www.velkincorp.com</p>
  </section>
</body>
</html>
```